FACEBOOK PAGE FOR QUILLON PLUMBING GROUP

We need a facebook banner for our new plumbing business.

Needs to be catchy and inline with our logo.

Phone: 0491 726 384
Email: hello@quillon.com.au
website: www.quillon.com.au
Servicing: Perth Metro Areas and surrounding suburbs
Services:
*We offer a wide range of services, including:
Plumbing – General maintenance, blocked drains, toilet repairs, burst pipes, reticulation, renovations & emergencies.

*Hot Water – Installation, servicing & repairs for all systems.

*Cooling & Heating – Air conditioning, evaporative cooling & heater servicing.

*Filtration – Filtered taps, under-sink systems & whole-house filtration setups.

Our Mission

Quillon Group believes plumbing shouldn't break the bank - or your trust. Our mission is to provide honest, affordable, and no-nonsense plumbing services that get the job done right the first time. No runaround - just reliable work, and the respect every customer deserves.

What Makes Us Different???

Upfront Fixed Pricing
No surprises, no hidden fees. You get clear, honest quotes before any work begins.

Respectful, Customer-First Service
We show up on time, communicate clearly, and treat your property like it’s our own.

Locals Serving Locals
We’re proud to support the Perth community with reliable, high-quality plumbing backed by real local care.

FOR THE DESIGNER A little background on us as a new biz for your reference:
By Locals, For Locals
After 13 years in the plumbing industry, seasoned local plumber Marcus founded his company to address the widespread issue of homeowners and businesses being overcharged or receiving inferior work. He knew there had to be a better way—and that’s when Quillon was created.
Today, Quillon Group is a trusted plumbing company based in Osborne Park, proudly serving residential, commercial, and industrial clients across the Perth metro area. With over a decade of experience, we deliver expert workmanship, fair pricing, and treat every job—big or small—with the same care and professionalism.
Need it done right—and affordably? Sort it with QUILLON today!

```html
<!DOCTYPE html>
<html lang="en">
<head>
<meta charset="utf-8">
<title>Quillon Plumbing Group – Facebook Cover</title>
<link href="https://fonts.googleapis.com/css2?family=Bebas+Neue&family=Montserrat:wght@400;500;600;700&display=swap" rel="stylesheet">
<style>
  :root {
    --stage: #8fadd6;
    --paper: #f4f6f8;
    --paper-tint: #dcedf7;
    --ink: #15151f;
    --navy: #2a1f6b;
    --brand-blue: #0a5fae;
    --brand-blue-light: #1a8fd6;
    --tick: #1ea0e6;
    --band: #000000;
    --white: #ffffff;
    --pipe-grey: #8a8d92;
  }
  * { box-sizing: border-box; margin: 0; padding: 0; }
  html, body { width: 1200px; height: 613px; overflow: hidden; }
  body { background: var(--stage); position: relative; font-family: "Montserrat", sans-serif; }

  .cover {
    position: absolute; left: 0; top: 78px; width: 1200px; height: 456px;
    overflow: hidden;
    background:
      radial-gradient(ellipse 420px 300px at 1060px 180px, rgba(220,237,247,0.9), transparent 70%),
      radial-gradient(ellipse 380px 240px at 330px 40px, rgba(214,236,248,0.8), transparent 70%),
      linear-gradient(180deg, var(--paper) 0%, #f7f8f9 100%);
  }
  .cover__base-strip {
    position: absolute; left: 420px; right: 0; top: 421px; bottom: 0;
    background: linear-gradient(90deg, transparent, var(--paper-tint) 60%);
  }

  .brand { position: absolute; left: 43px; top: 58px; color: var(--navy); font-weight: 700; }
  .brand__name { display: flex; align-items: center; gap: 12px; font-size: 58px; letter-spacing: 10px; line-height: 1; }
  .brand__dot { width: 18px; height: 18px; border-radius: 50%; background: var(--navy); }
  .brand__tagline { margin-top: 14px; font-size: 14px; letter-spacing: 9.4px; line-height: 1; }

  .band {
    position: absolute; left: 291px; right: 0; top: 332px; height: 89px;
    background: var(--band);
  }

  .illustration {
    position: absolute; left: 174px; top: 0; width: 488px; height: 456px;
    background:
      radial-gradient(ellipse 120px 90px at 430px 250px, rgba(247,131,45,0.55), transparent 70%),
      radial-gradient(ellipse 90px 120px at 60px 180px, rgba(40,110,190,0.45), transparent 70%),
      radial-gradient(ellipse 100px 90px at 300px 380px, rgba(30,110,200,0.45), transparent 70%),
      linear-gradient(160deg, rgba(138,141,146,0.35), rgba(138,141,146,0.55) 50%, rgba(138,141,146,0.3));
    border-radius: 6px;
  }

  .headline { position: absolute; left: 731px; top: 60px; font-family: "Bebas Neue", sans-serif; color: var(--ink); }
  .headline__lead { font-size: 47px; line-height: 44px; letter-spacing: -0.5px; }
  .headline__cta { position: absolute; left: -8px; top: 88px; display: flex; align-items: flex-end; white-space: nowrap; }
  .headline__pill {
    display: inline-block; background: var(--band); color: var(--white);
    font-family: "Montserrat", sans-serif; font-weight: 700; font-size: 21px;
    padding: 9px 14px 10px; border-radius: 6px; transform: rotate(-4deg);
    margin-right: 2px; margin-bottom: 6px;
  }
  .headline__brand {
    font-size: 68px; line-height: 56px; letter-spacing: -0.5px;
    background: linear-gradient(90deg, var(--brand-blue), var(--brand-blue-light));
    -webkit-background-clip: text; background-clip: text; color: transparent;
  }

  .services {
    position: absolute; left: 752px; top: 222px; width: 440px;
    display: grid; grid-template-columns: 168px 1fr; column-gap: 0;
    list-style: none; color: var(--ink); font-size: 17.5px; line-height: 25px;
  }
  .services li { position: relative; padding-left: 18px; margin-bottom: 10px; }
  .services li svg { position: absolute; left: -2px; top: -4px; width: 14px; height: 14px; }

  .contact { position: absolute; top: 332px; height: 89px; color: var(--white); }
  .contact--phone { left: 736px; display: flex; align-items: center; gap: 10px; font-size: 25px; font-weight: 600; letter-spacing: -0.5px; }
  .contact--phone svg { width: 20px; height: 20px; }
  .contact__divider { position: absolute; left: 939px; top: 344px; width: 2px; height: 59px; background: var(--white); }
  .contact--online { left: 962px; padding-top: 17px; font-size: 17px; font-weight: 500; }
  .contact--online p { display: flex; align-items: center; gap: 10px; height: 30px; }
  .contact--online svg { width: 14px; height: 14px; }
</style>
</head>
<body>
  <main class="cover">
    <div class="cover__base-strip"></div>

    <div class="band"></div>

    <div class="illustration" role="img" aria-label="Illustration of grey plumbing pipes with a red valve, radiator and wall water heater, with plumbers in blue overalls working at an orange sink cabinet"></div>

    <div class="brand">
      <div class="brand__name">QUILLON <span class="brand__dot"></span></div>
      <div class="brand__tagline">PLUMBING GROUP</div>
    </div>

    <h1 class="headline">
      <span class="headline__lead">NEED IT DONE RIGHT<br>AND AFFORDABLY?</span>
      <span class="headline__cta">
        <span class="headline__pill">Sort it with</span>
        <span class="headline__brand">QUILLON TODAY!</span>
      </span>
    </h1>

    <ul class="services">
      <li><svg viewBox="0 0 14 14"><path d="M1 7.5l4 4L13 2" fill="none" stroke="var(--tick)" stroke-width="2.2"/></svg>Plumbing</li>
      <li><svg viewBox="0 0 14 14"><path d="M1 7.5l4 4L13 2" fill="none" stroke="var(--tick)" stroke-width="2.2"/></svg>Filtration</li>
      <li><svg viewBox="0 0 14 14"><path d="M1 7.5l4 4L13 2" fill="none" stroke="var(--tick)" stroke-width="2.2"/></svg>Hot Water<br>Installation</li>
      <li><svg viewBox="0 0 14 14"><path d="M1 7.5l4 4L13 2" fill="none" stroke="var(--tick)" stroke-width="2.2"/></svg>Cooling &amp;<br>Heating</li>
    </ul>

    <div class="contact contact--phone">
      <svg viewBox="0 0 24 24"><path fill="var(--tick)" d="M6.6 10.8a15.1 15.1 0 0 0 6.6 6.6l2.2-2.2c.3-.3.7-.4 1-.2 1.1.4 2.3.6 3.6.6.6 0 1 .4 1 1V20c0 .6-.4 1-1 1A17 17 0 0 1 3 4c0-.6.4-1 1-1h3.5c.6 0 1 .4 1 1 0 1.3.2 2.5.6 3.6.1.3 0 .7-.2 1l-2.3 2.2z"/></svg>
      0491 726 384
    </div>
    <div class="contact__divider"></div>
    <div class="contact contact--online">
      <p><svg viewBox="0 0 16 12"><path fill="var(--tick)" d="M0 0h16v1.5L8 6.5 0 1.5zM0 3.3l8 5 8-5V12H0z"/></svg>hello@quillon.com.au</p>
      <p><svg viewBox="0 0 12 16"><path fill="var(--tick)" d="M1 0l10 9.5H6.5l2.5 5.2-2 .9-2.5-5.3L1 13.5z"/></svg>www.quillon.com.au</p>
    </div>
  </main>
</body>
</html>
```